Velmora Flowers Florist Flyer

We are requiring a flyer that advertises and promotes our new business. We specialise in weddings and events but would also like to branch out to corporates and an online subscription. Our brand is feminine/romantic with a touch of elegance and luxury. Our main colour schemes are white, black, gold and pale pink. Instagram: Velmora_flowers and website www.velmoraflowers.com.au
Target Market(s)
brides to be, females
Industry/Entity Type
Florist
Font styles to use
Sans Serif
Script
Other font styles liked:
- The Carpenter
Colors
ffffff
000000
333333
Requirements
Must have
- Feminine/romantic feel, through use of theme colours and elegant font
- our contact details Ph: 0478215096
- email address: contactus@velmoraflowers.com.au
Nice to have
- a description of us willing to work with clients to create their dream wedding flowers. That we offer consultations and no obligation quotes.

```html
<!DOCTYPE html>
<html lang="en">
<head>
<meta charset="utf-8">
<title>Velmora Flowers – Weddings and Events Flyer</title>
<link rel="stylesheet" href="https://fonts.googleapis.com/css2?family=Great+Vibes&family=Cormorant+Garamond:wght@500&family=Courgette&display=swap">
<style>
  :root {
    --blush: #f5d5e4;
    --blush-deep: #e9b3cb;
    --rose-line: #e7a3c2;
    --ink: #1d1a1b;
    --text-dark: #333333;
    --footer: #2a2325;
    --footer-text: #f2bfd7;
    --icon-pink: #efa9c9;
    --white: #ffffff;
  }
  * { margin: 0; padding: 0; box-sizing: border-box; }
  html, body { width: 846px; height: 1200px; overflow: hidden; background: var(--white); }
  .flyer {
    position: relative;
    width: 846px;
    height: 1200px;
    overflow: hidden;
    background: var(--blush);
  }
  .hero-photo {
    position: absolute;
    left: 0; top: 0;
    width: 846px; height: 560px;
    background:
      radial-gradient(ellipse 300px 190px at 380px 220px, #f4f1ea 0%, #c9d1bd 45%, rgba(120,140,110,0) 80%),
      radial-gradient(ellipse 140px 120px at 720px 220px, #eeece6 0%, rgba(200,200,190,0) 80%),
      linear-gradient(180deg, #c9b8a3 0%, #e2d5c5 40%, #eeeae6 100%);
  }
  .blush-curve {
    position: absolute;
    left: 0; top: 440px;
    width: 846px; height: 360px;
  }
  .brand-name {
    position: absolute;
    left: 0; width: 846px; top: 505px;
    text-align: center;
    font-family: "Great Vibes", cursive;
    font-size: 128px;
    line-height: 1;
    color: var(--ink);
  }
  .brand-sub {
    position: absolute;
    left: 0; width: 846px; top: 688px;
    padding-left: 40px;
    text-align: center;
    font-family: "Cormorant Garamond", serif;
    font-weight: 500;
    font-size: 34px;
    letter-spacing: 28px;
    color: var(--ink);
  }
  .tagline {
    position: absolute;
    left: 0; width: 846px; top: 760px;
    text-align: center;
    font-family: "Courgette", cursive;
    font-size: 20px;
    color: var(--text-dark);
  }
  .rule {
    position: absolute;
    left: 0; width: 846px;
    background: var(--rose-line);
  }
  .rule.thin { height: 2px; }
  .rule.thick { height: 5px; }
  .gallery-band {
    position: absolute;
    left: 0; top: 814px;
    width: 846px; height: 167px;
    background: linear-gradient(90deg, #e7b0c8, #f0c6d8 50%, #e7b0c8);
  }
  .gallery-photo {
    position: absolute;
    top: 826px; height: 144px;
    border: 2px solid var(--white);
  }
  .gallery-photo.bouquet-white { left: 38px; width: 202px;
    background: radial-gradient(ellipse 70px 55px at 85px 60px, #fbf3e6, #ecdcc8 60%, #d9d3ce); }
  .gallery-photo.crate-posy { left: 271px; width: 129px;
    background: radial-gradient(ellipse 55px 40px at 64px 50px, #f2cfb5, #aeb98f 60%, #ece8e3); }
  .gallery-photo.gold-urn { left: 433px; width: 198px;
    background: radial-gradient(ellipse 90px 45px at 100px 60px, #e9c9bb, #8e3a3c 45%, #c7b397 80%, #e9e4dc); }
  .gallery-photo.pastel-posy { left: 656px; width: 142px;
    background: radial-gradient(ellipse 55px 60px at 70px 65px, #f4f1ec, #c3cdd4 60%, #8c8c86); }
  .quote {
    position: absolute;
    left: 0; width: 846px; top: 1012px;
    text-align: center;
    font-family: "Courgette", cursive;
    font-size: 20px;
    line-height: 28px;
    color: var(--text-dark);
  }
  .quote-author {
    position: absolute;
    left: 540px; top: 1074px;
    font-family: "Courgette", cursive;
    font-size: 15px;
    color: var(--text-dark);
  }
  .contact-bar {
    position: absolute;
    left: 0; top: 1116px;
    width: 846px; height: 84px;
    background: var(--footer);
    display: flex;
    align-items: center;
    justify-content: space-between;
    padding: 0 20px;
  }
  .contact-item {
    display: flex;
    align-items: center;
    gap: 10px;
    font-family: "Courgette", cursive;
    font-size: 18px;
    color: var(--footer-text);
  }
  .contact-icon {
    width: 34px; height: 34px;
    flex: none;
  }
</style>
</head>
<body>
<main class="flyer">
  <div class="hero-photo" role="img" aria-label="Photo of tall white rose and greenery centrepieces on gold stands along a wedding reception table"></div>

  <svg class="blush-curve" viewBox="0 0 846 360" aria-hidden="true">
    <path d="M0 60 Q 400 -30 846 80 L846 360 L0 360 Z" fill="var(--blush)"/>
    <path d="M300 10 Q 520 0 700 40" fill="none" stroke="#ffffff" stroke-opacity="0.7" stroke-width="3"/>
    <path d="M660 60 Q 780 80 846 110" fill="none" stroke="#ffffff" stroke-width="4"/>
  </svg>

  <h1 class="brand-name">Velmora</h1>
  <p class="brand-sub">FLOWERS</p>
  <p class="tagline">Creating stunning Flowers for Weddings and Events</p>

  <div class="rule thin" style="top:800px"></div>
  <div class="rule thick" style="top:807px"></div>
  <div class="gallery-band"></div>
  <div class="gallery-photo bouquet-white" role="img" aria-label="Photo of a round bridal bouquet of cream roses"></div>
  <div class="gallery-photo crate-posy" role="img" aria-label="Photo of peach roses arranged in a rustic wooden crate"></div>
  <div class="gallery-photo gold-urn" role="img" aria-label="Photo of red and blush roses in a gold urn"></div>
  <div class="gallery-photo pastel-posy" role="img" aria-label="Photo of a white and pale blue bridal posy"></div>
  <div class="rule thick" style="top:981px"></div>
  <div class="rule thin" style="top:990px"></div>

  <p class="quote">Design is not making beauty, beauty emerges from selection,<br>affinities, integration, love.</p>
  <p class="quote-author">– Lena Marsh</p>

  <footer class="contact-bar">
    <div class="contact-item">
      <svg class="contact-icon" viewBox="0 0 34 34" aria-hidden="true">
        <circle cx="17" cy="17" r="17" fill="var(--icon-pink)"/>
        <path d="M11 9 l4 0 l1.5 4.5 l-2.5 1.8 q1.8 3.7 5.5 5.5 l1.8 -2.5 l4.5 1.5 l0 4 q-1 1.5 -3 1.5 q-12 -1 -13 -13 q0 -2 1.2 -3.3z" fill="var(--white)"/>
      </svg>
      <span>0478215096</span>
    </div>
    <div class="contact-item">
      <svg class="contact-icon" viewBox="0 0 34 34" aria-hidden="true">
        <circle cx="17" cy="17" r="17" fill="var(--icon-pink)"/>
        <rect x="8" y="11" width="18" height="13" rx="1.5" fill="var(--white)"/>
        <path d="M8.5 12 L17 19 L25.5 12" fill="none" stroke="var(--icon-pink)" stroke-width="1.6"/>
      </svg>
      <span>contactus@velmoraflowers.com.au</span>
    </div>
    <div class="contact-item">
      <svg class="contact-icon" viewBox="0 0 34 34" aria-hidden="true">
        <circle cx="17" cy="17" r="17" fill="var(--icon-pink)"/>
        <g fill="none" stroke="var(--white)" stroke-width="1.6">
          <circle cx="17" cy="17" r="9"/>
          <ellipse cx="17" cy="17" rx="4" ry="9"/>
          <line x1="8" y1="17" x2="26" y2="17"/>
          <path d="M10 12 h14 M10 22 h14"/>
        </g>
      </svg>
      <span>www.velmoraflowers.com.au</span>
    </div>
  </footer>
</main>
</body>
</html>
```